ESCORT DIRECTORY

This website is an advertising and information resource , we only sell advertisement space.
The requirement:
-- 7 Banners with different size
--sexy girl on the banner
-- the sexy girl will have different position on each banner
--I want my logo on the banner (Upload files)
-- I want the word : " ADVERTISE FOR FREE" in a beautiful presentation

```html
<!DOCTYPE html>
<html lang="en">
<head>
<meta charset="utf-8">
<title>Nocturelle – Advertise for Free banners</title>
<link rel="stylesheet" href="https://fonts.googleapis.com/css2?family=Kaushan+Script&family=Josefin+Sans:wght@300&display=swap">
<style>
  :root {
    --page: #ffffff;
    --ink: #111111;
    --pink: #ff1a8c;
    --pink-soft: #ff9fd0;
    --frame: #f08ac0;
    --logo-grey: #5a5a5a;
    --photo-sea-a: #c9d2d6;
    --photo-sea-b: #e3e8ea;
    --photo-dark-a: #1b1b1b;
    --photo-dark-b: #6a6a6a;
    --photo-skin-a: #c89a7e;
    --photo-skin-b: #efe2da;
    --panel-blue: #e6eef8;
    --swoosh: #b9d3f0;
    --curve-grey: #c8d0d3;
  }
  * { box-sizing: border-box; margin: 0; padding: 0; }
  html, body { width: 1200px; height: 788px; overflow: hidden; background: var(--page); }
  .canvas { position: relative; width: 1200px; height: 788px; }

  .banner {
    position: absolute;
    overflow: hidden;
    background: var(--page);
    border: 1px solid var(--frame);
    box-shadow: 3px 4px 6px rgba(0,0,0,.35);
  }
  .banner--leaderboard { left: 56px; top: 37px; width: 1065px; height: 219px; }
  .banner--square-dark { left: 56px; top: 341px; width: 439px; height: 366px; }
  .banner--square-light { left: 653px; top: 341px; width: 468px; height: 350px; }

  .photo { position: absolute; }
  .photo--sea { inset: 0; background: linear-gradient(180deg, var(--photo-sea-b), var(--photo-sea-a) 70%, var(--photo-sea-b)); }
  .photo--silhouette { left: 0; top: 0; width: 215px; height: 100%; background: radial-gradient(ellipse at 45% 55%, var(--photo-dark-b), var(--photo-dark-a) 70%); }
  .photo--bikini { right: 0; top: 0; width: 236px; height: 100%; background: radial-gradient(ellipse at 50% 45%, var(--photo-skin-a), var(--photo-skin-b) 75%, rgba(255,255,255,0) 100%); }

  .shape { position: absolute; }

  .brand {
    position: absolute;
    display: flex; flex-direction: column; align-items: center; gap: 12px;
    font-family: "Josefin Sans", sans-serif; font-weight: 300;
    color: var(--logo-grey); letter-spacing: 4px; white-space: nowrap;
  }
  .brand__mark { width: 44px; height: 44px; background: var(--pink); }

  .offer { position: absolute; font-family: "Kaushan Script", cursive; text-align: center; line-height: 1; white-space: nowrap; }
  .offer__line { display: block; color: var(--ink); }
  .offer__free { display: block; color: var(--pink); }

  .cta-bar { position: absolute; right: 0; bottom: 0; height: 22px; background: linear-gradient(90deg, var(--pink), var(--pink-soft)); }
  .panel-blue { position: absolute; left: 0; right: 0; bottom: 0; top: 134px; background: var(--panel-blue); }
</style>
</head>
<body>
<main class="canvas">

  <section class="banner banner--leaderboard">
    <div class="photo photo--sea" role="img" aria-label="Photo of a woman in a swimsuit reclining on shallow water"></div>
    <svg class="shape" width="240" height="219" viewBox="0 0 240 219" aria-hidden="true">
      <path d="M0 0 H200 Q250 110 222 219 H0 Z" fill="var(--curve-grey)"/>
      <path d="M0 0 H186 Q234 110 208 219 H0 Z" fill="var(--page)"/>
    </svg>
    <div class="brand" style="left:16px; top:56px; font-size:19px;">
      <span class="brand__mark"></span>
      <span>NOCTURELLE</span>
    </div>
    <p class="offer" style="right:40px; top:50px; text-align:right;">
      <span class="offer__line" style="font-size:36px;">ADVERTISE FOR</span>
      <span class="offer__free" style="font-size:64px; margin-top:6px;">FREE</span>
    </p>
  </section>

  <section class="banner banner--square-dark">
    <div class="photo photo--silhouette" role="img" aria-label="Black and white photo of a nude woman's back in silhouette"></div>
    <div class="brand" style="left:215px; width:224px; top:36px; font-size:18px;">
      <span class="brand__mark"></span>
      <span>NOCTURELLE</span>
    </div>
    <p class="offer" style="left:225px; width:208px; top:152px;">
      <span class="offer__line" style="font-size:28px;">ADVERTISE</span>
      <span class="offer__line" style="font-size:28px; margin-top:22px;">FOR</span>
      <span class="offer__free" style="font-size:56px; margin-top:12px;">FREE</span>
    </p>
    <div class="cta-bar" style="left:215px;"></div>
  </section>

  <section class="banner banner--square-light">
    <div class="panel-blue"></div>
    <svg class="shape" style="left:170px; top:0;" width="298" height="350" viewBox="0 0 298 350" aria-hidden="true">
      <path d="M20 0 Q120 120 70 350" fill="none" stroke="var(--swoosh)" stroke-width="22" opacity=".7"/>
      <path d="M50 0 Q150 140 110 350" fill="none" stroke="var(--swoosh)" stroke-width="6" opacity=".8"/>
    </svg>
    <div class="photo photo--bikini" role="img" aria-label="Photo of a smiling woman in a grey bikini posing with one arm extended"></div>
    <div class="brand" style="left:30px; width:200px; top:24px; font-size:18px;">
      <span class="brand__mark"></span>
      <span>NOCTURELLE</span>
    </div>
    <p class="offer" style="left:30px; width:185px; top:165px;">
      <span class="offer__line" style="font-size:27px;">ADVERTISE</span>
      <span class="offer__line" style="font-size:27px; margin-top:22px;">FOR</span>
      <span class="offer__free" style="font-size:52px; margin-top:10px;">FREE</span>
    </p>
  </section>

</main>
</body>
</html>
```